Cybersecurity company is looking for business card.

I need a business card design for our company, we are a cybersecurity company providing advance technology to protect agains any kind of malware. We need a fresh modern design it should communicate modern, technology and growth.

Target Market(s)

Business to business

Industry/Entity Type

Business

Contact Information for Business Card

Should have location, address, fax, mobile, phone, email and website.

Requirements
Must have
• Must follow company's logo color and style. Must have the company's log on its.

```html
<!DOCTYPE html>
<html lang="en">
<head>
<meta charset="utf-8">
<title>Vextrel business card</title>
<link href="https://fonts.googleapis.com/css2?family=Quicksand:wght@500;700&display=swap" rel="stylesheet">
<style>
  :root {
    --backdrop: #e4e6e9;
    --card-white: #ffffff;
    --card-black: #050505;
    --ink: #0a0a0a;
    --paper-text: #ffffff;
    --red-bright: #a31916;
    --red-deep: #5c1612;
  }
  * { margin: 0; padding: 0; box-sizing: border-box; }
  html, body {
    width: 1200px; height: 1000px; overflow: hidden;
    background: var(--backdrop);
    font-family: "Quicksand", sans-serif;
  }
  .canvas { position: relative; width: 1200px; height: 1000px; }
  .card {
    position: absolute; left: 313px; width: 562px; height: 347px; overflow: hidden;
  }
  .card--front { top: 125px; background: var(--card-white); }
  .card--back { top: 521px; background: var(--card-black); }

  .brand-name {
    position: absolute; font-family: "Quicksand", sans-serif; font-weight: 700;
    letter-spacing: 1px; line-height: 1;
  }
  .card--front .brand-name {
    left: 0; right: 0; top: 132px; text-align: center; font-size: 84px; color: var(--ink);
  }
  .card--back .brand-name {
    left: 99px; top: 96px; font-size: 34px; color: var(--paper-text);
  }

  .accent-field {
    position: absolute; inset: 0;
    background: linear-gradient(158deg, var(--card-black) 0%, var(--card-black) 52%, var(--red-deep) 74%, var(--red-bright) 100%);
  }

  .contact-list {
    position: absolute; left: 328px; top: 44px; list-style: none;
    color: var(--paper-text); font-size: 11.5px; font-weight: 500; letter-spacing: 0.4px;
  }
  .contact-item { position: relative; padding-left: 27px; line-height: 1.35; }
  .contact-item svg { position: absolute; left: 0; top: 1px; width: 14px; height: 14px; fill: var(--red-bright); }
  .contact-item--address { margin-bottom: 24px; }
  .contact-item--address .line-gap { display: block; margin-top: 4px; }
  .contact-item--email { margin-bottom: 27px; }
  .contact-item--mobile { margin-bottom: 24px; letter-spacing: 1.6px; }
  .contact-item--phone { letter-spacing: 1.6px; }

  .website {
    position: absolute; left: 0; right: 0; bottom: 5px; text-align: center;
    color: var(--paper-text); font-size: 15.5px; font-weight: 500; letter-spacing: 2.6px;
  }
</style>
</head>
<body>
<main class="canvas">
  <section class="card card--front" aria-label="Card front">
    <div class="brand-name">Vextrel</div>
  </section>

  <section class="card card--back" aria-label="Card back">
    <div class="accent-field" role="img" aria-label="Decorative red geometric pattern"></div>

    <div class="brand-name">Vextrel</div>

    <ul class="contact-list">
      <li class="contact-item contact-item--address">
        <svg viewBox="0 0 14 14"><path d="M7 2 L13 7 H11 V12 H3 V7 H1 Z"/></svg>
        Harbor Tech Park (HTP) -<br>Meridian Avenue.<span class="line-gap">Coastal City - UAE</span>
      </li>
      <li class="contact-item contact-item--email">
        <svg viewBox="0 0 14 14"><path d="M1 3 H13 V11 H1 Z M2 4 L7 8 L12 4" stroke="#050505" stroke-width="0.9"/></svg>
        name.surname@vextrel.com
      </li>
      <li class="contact-item contact-item--mobile">
        <svg viewBox="0 0 14 14"><path d="M4 1 H10 V13 H4 Z M5 3 V9 H9 V3 Z"/></svg>
        +00 52 555 0142
      </li>
      <li class="contact-item contact-item--phone">
        <svg viewBox="0 0 14 14"><path d="M4 1 H10 V5 H13 V12 H1 V5 H4 Z M5 2 V5 H9 V2 Z"/></svg>
        04 555 0178<br>04 555 0179
      </li>
    </ul>

    <div class="website">www.vextrel.com</div>
  </section>
</main>
</body>
</html>
```